依頼概要
第33回白鷺川大星火大会
2018年7月14日(土)午後7時30分開会
関東最大級22800発
三大花火師夢の饗宴 桐原煙火工業・宮田火工製作所・藤屋松井火工店
主催:北浜町観光協会・きたはまみなと祭り実行委員会
後援:北浜町・北浜町議会・七森町・北浜町商工会・七森町商工会・JA北陸あおば
問い合わせ:北浜町観光協会 TEL0280-81-1319
北浜町で検索的なもの
観覧チケットの購入はチケミナで検索的なもの

若干の構成を再度お願いする場合もあります。また、制作いただきました作品に、場合によりこちらで後援や開催日時等軽微な修正をする場合があります。
http://filevault-sample.jp/photo/3c1a9e07b42d58f6a0e9c2147bd86f03e5a1c9d2
上記URLは添付にあるものと同様の使用する写真です

町長様・観光協会様の方で候補作品から選んでいただきました。

ご参加・ご協力ありがとうございました。

```html
<!DOCTYPE html>
<html lang="ja">
<head>
<meta charset="utf-8">
<title>第33回白鷺川大星火大会</title>
<link rel="stylesheet" href="https://fonts.googleapis.com/css2?family=Shippori+Mincho+B1:wght@600;800&family=Noto+Sans+JP:wght@400;700;900&display=swap">
<style>
  :root {
    --night: #050406;
    --gold: #e7c25a;
    --white: #ffffff;
    --soft: #d9d6de;
    --violet: #b08ad8;
    --field: #ffffff;
    --ink: #111111;
    --rule: #5a5660;
  }
  * { margin: 0; padding: 0; box-sizing: border-box; }
  html, body { width: 841px; height: 1200px; overflow: hidden; background: var(--night); }
  .poster {
    position: relative; width: 841px; height: 1200px; overflow: hidden;
    background: var(--night); color: var(--white);
    font-family: "Shippori Mincho B1", "Noto Serif JP", serif;
  }
  .masters { position: absolute; top: 26px; width: 100%; text-align: center; color: var(--gold); font-family: "Noto Sans JP", sans-serif; font-weight: 700; }
  .masters__title { font-size: 24px; letter-spacing: 4px; line-height: 1.3; }
  .masters__makers { font-size: 19px; margin-top: 4px; line-height: 1.3; }
  .headline { position: absolute; top: 110px; width: 100%; text-align: center; }
  .headline__lead { font-size: 40px; font-weight: 800; letter-spacing: 2px; line-height: 1.2; }
  .headline__lead small { font-size: 26px; }
  .headline__count { font-size: 112px; font-weight: 800; line-height: 1.1; letter-spacing: 2px; }
  .fireworks {
    position: absolute; top: 340px; left: 0; width: 841px; height: 610px;
    background:
      radial-gradient(ellipse 30% 25% at 50% 28%, rgba(255,240,220,.55), transparent 70%),
      radial-gradient(ellipse 22% 20% at 25% 35%, rgba(235,140,120,.35), transparent 70%),
      radial-gradient(ellipse 22% 20% at 75% 35%, rgba(235,140,120,.35), transparent 70%),
      radial-gradient(ellipse 60% 14% at 50% 86%, rgba(170,90,220,.55), transparent 75%),
      radial-gradient(ellipse 50% 30% at 50% 65%, rgba(255,200,140,.25), transparent 70%),
      var(--night);
  }
  .event { position: absolute; top: 948px; left: 0; width: 100%; height: 110px; }
  .event__line { position: absolute; left: 0; top: 40px; width: 120px; height: 4px; background: var(--violet); }
  .event__edition { position: absolute; left: 128px; top: 28px; font-size: 20px; font-weight: 800; line-height: 1; }
  .event__name { position: absolute; left: 200px; top: 0; font-size: 66px; font-weight: 800; letter-spacing: 2px; line-height: 1;
    color: var(--white); text-shadow: 0 0 10px rgba(176,138,216,.6); white-space: nowrap; }
  .event__date { position: absolute; left: 250px; top: 76px; font-size: 24px; font-weight: 800; letter-spacing: 1px; line-height: 1.2; white-space: nowrap; }
  .event__date b { font-size: 32px; }
  .contact { position: absolute; top: 1064px; left: 22px; right: 22px; height: 80px; display: flex; justify-content: space-between; align-items: flex-start; font-family: "Noto Sans JP", sans-serif; }
  .contact__head { line-height: 1.3; white-space: nowrap; }
  .contact__label { font-size: 13px; }
  .contact__org { font-size: 15px; font-weight: 700; margin-left: 10px; }
  .contact__phone { display: flex; align-items: center; gap: 6px; margin-top: 4px; font-size: 32px; font-weight: 900; line-height: 1.1; white-space: nowrap; }
  .contact__hours { font-size: 9px; color: var(--soft); line-height: 1.3; }
  .search { display: grid; grid-template-columns: auto auto; gap: 6px 8px; font-size: 12px; align-items: center; white-space: nowrap; }
  .search__box { display: flex; align-items: center; gap: 4px; }
  .search__field { background: var(--field); color: var(--ink); width: 100px; height: 20px; padding-left: 5px; font-size: 12px; line-height: 20px; font-weight: 700; }
  .credits { position: absolute; top: 1156px; left: 22px; right: 22px; padding-top: 8px; border-top: 1px solid var(--rule); font-family: "Noto Sans JP", sans-serif; font-size: 10px; line-height: 1.4; color: var(--soft); white-space: nowrap; }
</style>
</head>
<body>
<main class="poster">
  <header class="masters">
    <p class="masters__title">三大花火師夢の饗宴</p>
    <p class="masters__makers">桐原煙火工業・宮田火工製作所・藤屋松井火工店による</p>
  </header>

  <section class="headline">
    <p class="headline__lead">関東最大級<small>の</small>花火</p>
    <p class="headline__count">「22,800発」</p>
  </section>

  <div class="fireworks" role="img" aria-label="夜空に広がる色とりどりの打ち上げ花火と水面のスターマイン"></div>

  <section class="event">
    <span class="event__line"></span>
    <span class="event__edition">第33回</span>
    <h1 class="event__name">白鷺川大星火大会</h1>
    <p class="event__date">'18年 <b>7</b>月<b>14</b>日(土) <b>7:30</b></p>
  </section>

  <section class="contact">
    <div class="contact__info">
      <p class="contact__head"><span class="contact__label">お問合わせ先</span><span class="contact__org">北浜町観光協会</span></p>
      <p class="contact__phone">
        <svg width="24" height="24" viewBox="0 0 24 24" aria-hidden="true"><path fill="#fff" d="M6.6 10.8a15 15 0 0 0 6.6 6.6l2.2-2.2c.3-.3.7-.4 1-.2 1.1.4 2.3.6 3.6.6.6 0 1 .4 1 1V20c0 .6-.4 1-1 1A17 17 0 0 1 3 4c0-.6.4-1 1-1h3.5c.6 0 1 .4 1 1 0 1.3.2 2.5.6 3.6.1.3 0 .7-.2 1z"/></svg>
        0290-64-7725
      </p>
      <p class="contact__hours">受付時間 平日 9:00〜17:00</p>
    </div>
    <div class="search">
      <span>・花火大会についての詳細は</span>
      <span class="search__box"><span class="search__field">北浜町</span>で検索</span>
      <span>・観覧チケットの購入は</span>
      <span class="search__box"><span class="search__field">チケミナ</span>で検索</span>
    </div>
  </section>

  <footer class="credits">主催｜北浜町観光協会・きたはまみなと祭り実行委員会　後援｜北浜町・北浜町議会・七森町・北浜町商工会・七森町商工会・JA北陸あおば</footer>
</main>
</body>
</html>
```